New Webpage for High Class Expert Witness Services Company

We are looking for a minimalist design for a webpage that just has our logo and an entry form offer to connect with one of our Liaisons.
The entry form should just ask for Name, Email, Contact Info and Description of Project.

Company Name is: The Marlow Crest Advisory Services

Number of Pages Required

1 page

```html
<!DOCTYPE html>
<html lang="en">
<head>
<meta charset="utf-8">
<title>The Marlow Crest Advisory Services – Connect with a Liaison</title>
<link rel="stylesheet" href="https://fonts.googleapis.com/css2?family=Cinzel:wght@500&family=Playfair+Display:wght@400;700&family=Roboto:wght@400&display=swap">
<style>
  :root {
    --page-bg: #131313;
    --page-bg-edge: #0e0e0e;
    --below-fold: #ffffff;
    --frame-line: #bdbdbd;
    --heading: #d4d4d6;
    --body-text: #ffffff;
    --label: #ffffff;
    --field-bg: #ffffff;
    --field-line: #d0d0d0;
    --placeholder: #9a9a9a;
    --button-bg: #c1c2c4;
    --button-text: #1a1a1a;
    --footer-text: #d2d2d2;
  }
  * { box-sizing: border-box; margin: 0; padding: 0; }
  html, body {
    width: 1200px; height: 2222px; overflow: hidden;
    background: var(--below-fold);
  }
  .page {
    position: relative; width: 1200px; height: 2155px;
    background: radial-gradient(ellipse at 50% 40%, var(--page-bg) 55%, var(--page-bg-edge) 100%);
  }
  .frame {
    position: absolute; left: 54px; top: 98px; width: 1091px; height: 1960px;
    border: 1px solid var(--frame-line); border-radius: 8px;
  }
  .brand {
    position: absolute; left: 54px; top: 140px; width: 1091px; height: 160px;
    display: flex; align-items: center; justify-content: center; gap: 34px;
  }
  .brand-mark { width: 110px; height: 110px; background: var(--heading); flex: none; }
  .brand-name {
    font-family: "Cinzel", serif; font-weight: 500; font-size: 54px; line-height: 1.15;
    color: var(--heading); letter-spacing: 2px; text-transform: uppercase;
  }
  .intro-title {
    position: absolute; left: 54px; width: 1091px; top: 465px;
    font-family: "Cinzel", serif; font-weight: 500; font-size: 49px;
    color: var(--heading); text-align: center; white-space: nowrap;
  }
  .intro-text {
    position: absolute; left: 66px; top: 569px; width: 1068px;
    font-family: "Roboto", sans-serif; font-size: 31px; line-height: 51px;
    color: var(--body-text); text-align: justify;
  }
  .contact-form {
    position: absolute; left: 66px; top: 898px; width: 1066px; height: 896px;
    border: 1px solid var(--frame-line); border-radius: 8px;
  }
  .field-label {
    position: absolute; left: 22px;
    font-family: "Playfair Display", serif; font-weight: 700; font-size: 31px;
    color: var(--label); text-transform: uppercase; letter-spacing: -0.5px;
  }
  .field-input {
    position: absolute; left: 22px; width: 1022px; height: 83px;
    background: var(--field-bg); border: 1px solid var(--field-line); border-radius: 4px;
    padding: 0 34px; font-family: "Roboto", sans-serif; font-size: 29px; color: #222;
  }
  .field-input::placeholder, .field-area::placeholder { color: var(--placeholder); }
  .field-area {
    position: absolute; left: 22px; width: 1022px; height: 202px;
    background: var(--field-bg); border: 1px solid var(--field-line); border-radius: 4px;
    padding: 14px 30px; font-family: "Roboto", sans-serif; font-size: 29px; resize: vertical;
  }
  .submit-button {
    position: absolute; left: 22px; top: 789px; width: 1022px; height: 84px;
    background: var(--button-bg); border: none; border-radius: 4px;
    font-family: "Playfair Display", serif; font-size: 31px; color: var(--button-text);
    text-transform: uppercase;
  }
  .site-footer {
    position: absolute; left: 54px; top: 1948px; width: 1091px;
    font-family: "Playfair Display", serif; font-size: 33px; line-height: 52px;
    font-variant: small-caps; color: var(--footer-text); text-align: center;
  }
</style>
</head>
<body>
<main class="page">
  <div class="frame"></div>

  <header class="brand">
    <div class="brand-mark"></div>
    <div class="brand-name">The Marlow Crest<br>Advisory Services</div>
  </header>

  <h1 class="intro-title">CONNECT WITH ONE OF OUR LIAISONS</h1>
  <p class="intro-text">Lorem ipsum dolor sit amet, consectetur adipiscing elit, sed do eiusmod tempor incididunt ut labore et dolore magna aliqua. Vulputate dignissim suspendisse in est ante. Faucibus turpis in eu mi bibendum neque. Sodales ut etiam sit amet nisl purus. Velit laoreet id donec ultrices tincidunt.</p>

  <form class="contact-form">
    <label class="field-label" style="top:20px" for="name">Name</label>
    <input class="field-input" style="top:78px" id="name" type="text" placeholder="Name">

    <label class="field-label" style="top:182px" for="email">Email</label>
    <input class="field-input" style="top:240px" id="email" type="email" placeholder="Type your Email">

    <label class="field-label" style="top:344px" for="contact">Contact Info</label>
    <input class="field-input" style="top:402px" id="contact" type="text" placeholder="Type your contact information">

    <label class="field-label" style="top:506px" for="project">Description of Project</label>
    <textarea class="field-area" style="top:564px" id="project" placeholder="Describe about your project."></textarea>

    <button class="submit-button" type="submit">Submit</button>
  </form>

  <footer class="site-footer">Copyright © 2026 &amp; Powered by The Marlow Crest<br>Advisory Services</footer>
</main>
</body>
</html>
```